Catchy Cards for Hospital

I run a rural hospital in Texas called Pellor Valley Hospital and am in need of contemporary business cards for all of my Department Heads. While our logo is somewhat simplistic, I don't have the option of changing it at this time, so anything to make the rest of the card present the appearance of a modern, professional healthcare facility would be great. Although the attached files are in black, our hospital colors are in a copper brown and black. I need to be able to change the name and title on the card so I can get cards printed for various department heads.

Target Market(s)

Referring physicians, large hospital systems, national organizations, state and federal government

Industry/Entity Type

Hospital

Contact Information for Business Card

Name Dale Hoskin
Title CEO

Phone: Main 325-555-0147 & Direct xxxxxx
Fax xxxxx
dale.hoskin@pellorvh.example
382 Wimble Street Box 415
Brackton, Westmark 76902

Font styles to use
Serif

Colors
f48340

Requirements
Must have
• Clean crisp lines and ability to modify names, titles and emails
• On the back "PellorValleyHospital.Example
Nice to have
• Needs to be in line with logo, which is a bit dated and not too appealing, but I'm hoping that the rest of the card can make up for that fact just a little bit.
• Hospital's colors are a copper brown, black and white
Should not have
• Shapes or anything distracting

```html
<!DOCTYPE html>
<html lang="en">
<head>
<meta charset="utf-8">
<title>Pellor Valley Hospital – Business Card</title>
<link rel="stylesheet" href="https://fonts.googleapis.com/css2?family=Noto+Serif:wght@400;700&display=swap">
<style>
  :root {
    --copper: #f48340;
    --ink: #111111;
    --paper: #ffffff;
    --backdrop: #e4e4e4;
  }
  * { margin: 0; padding: 0; box-sizing: border-box; }
  html, body { width: 1200px; height: 900px; overflow: hidden; }
  body {
    background: var(--backdrop);
    font-family: "Noto Serif", Georgia, serif;
    color: var(--ink);
    position: relative;
  }
  .card {
    position: absolute;
    left: 250px;
    width: 700px;
    height: 400px;
    border-radius: 22px;
    overflow: hidden;
    box-shadow: 0 6px 18px rgba(0,0,0,0.18);
  }
  /* Back side */
  .card-back { top: 35px; background: var(--copper); color: var(--paper); }
  .card-back .hospital-name {
    position: absolute; left: 0; right: 0; top: 115px;
    text-align: center; font-weight: 700; font-size: 48px; line-height: 1.1;
  }
  .card-back .website {
    position: absolute; left: 0; right: 0; top: 280px;
    text-align: center; font-size: 20px;
  }
  /* Front side */
  .card-front { top: 465px; background: var(--paper); }
  .front-accent { position: absolute; left: 0; top: 0; width: 700px; height: 400px; }
  .person { position: absolute; left: 70px; top: 36px; }
  .person-name { font-weight: 700; font-size: 28px; line-height: 1.15; }
  .person-title { color: var(--copper); font-size: 18px; line-height: 1.2; }
  .address { position: absolute; left: 70px; top: 122px; font-size: 19px; line-height: 1.3; }
  .contacts { position: absolute; left: 70px; top: 186px; list-style: none; font-size: 19px; }
  .contacts li { display: flex; align-items: center; gap: 12px; height: 27px; }
  .contacts svg { width: 22px; height: 22px; flex: none; }
  .front-logo {
    position: absolute; right: 50px; top: 105px; width: 270px;
    font-weight: 700; font-size: 38px; line-height: 1.15; color: var(--ink);
  }
</style>
</head>
<body>

<section class="card card-back" aria-label="Card back">
  <p class="hospital-name">Pellor Valley<br>Hospital</p>
  <p class="website">PellorValleyHospital.Example</p>
</section>

<section class="card card-front" aria-label="Card front">
  <svg class="front-accent" viewBox="0 0 700 400" aria-hidden="true">
    <circle cx="0" cy="28" r="16" fill="#f48340"/>
    <rect x="0" y="318" width="470" height="10" fill="#111111"/>
    <path d="M0 334 H460 Q470 334 476 344 Q482 352 495 352 H700 V400 H0 Z" fill="#f48340"/>
  </svg>

  <div class="person">
    <p class="person-name">Dale Hoskin</p>
    <p class="person-title">CEO</p>
  </div>

  <p class="address">382 Wimble Street Box 415<br>Brackton, Westmark 76902</p>

  <ul class="contacts">
    <li>
      <svg viewBox="0 0 22 22"><rect width="22" height="22" rx="4" fill="#f48340"/><path d="M5 9 Q11 4 17 9 L15 11 L13 9 H9 L7 11 Z M7 12 H15 V17 H7 Z" fill="#fff"/></svg>
      325-555-0147
    </li>
    <li>
      <svg viewBox="0 0 22 22"><rect width="22" height="22" rx="4" fill="#f48340"/><path d="M8 5 L10 8 L9 10 Q10 13 12 14 L14 13 L17 15 L15 17 Q9 17 6 10 Q5 7 8 5 Z" fill="#fff"/></svg>
      123-456-789
    </li>
    <li>
      <svg viewBox="0 0 22 22"><rect width="22" height="22" rx="4" fill="#f48340"/><path d="M7 4 H15 V8 H7 Z M4 9 H18 V15 H15 V18 H7 V15 H4 Z" fill="#fff"/><rect x="8" y="12" width="6" height="4" fill="#f48340"/></svg>
      123-456-789
    </li>
    <li>
      <svg viewBox="0 0 22 22"><rect width="22" height="22" rx="4" fill="#f48340"/><rect x="4" y="6" width="14" height="10" fill="#fff"/><path d="M4 6 L11 12 L18 6" fill="none" stroke="#f48340" stroke-width="1.4"/></svg>
      dale.hoskin@pellorvh.example
    </li>
  </ul>

  <p class="front-logo">Pellor Valley<br>Hospital</p>
</section>

</body>
</html>
```